Bottle Label MCR for our own gin

Label for our own gin of "Le Cabinet Doré".
"Le Cabinet Doré" is a name that evokes the Victorian era and traditional medicine, which fits perfectly with the steampunk theme! This could inspire additional design elements, such as medicine bottles, laboratory jars or pharmaceutical symbols.
Updates

- The label need to be horizontal > width 10,65 cm x height 8,2 cm
- Steampunk airship logo in the centre LE CABINET DORÉ" in ornate brass lettering above the logo AWAKEN YOUR SENSES - FOLLOW YOUR WONDER ».
- With different inlays like zeppelin, balloon, …
- At bottom "Velmont Dry Gin" in classic letters.
- Details :
- 43% VOL > left side down
- e50 CL > right side down
- Steampunk style with zeppelin, balloon, chemicals bottles, ingredients
- Font styles : "ALGERIAN"
- IMPORTANT > In the logo of "LE CABNIET DORÉ" > please chage the word "COCKTAIL" by "TASTES"

Thank you in advance and good work,

JM

Target Market(s)

Sale of gin bottles worlwide

Industry/Entity Type

HORECA (Hotels, Bars, Restaurants)

Font styles to use
Decorative
Other font styles liked:
• ALGERIAN

Requirements
Must have
• Our existing logo of "Le Cabinet Doré"
Nice to have
• Steampunk airship logo in the centre LE CABINET DORÉ" in ornate brass lettering above the logo AWAKEN YOUR SENSES - FOLLOW YOUR WONDER" in cursive letters at bottom Velmont Dry Gin" in classic letters next to the logo 38% vol" and "50 cl" in smaller text at bottom right Size for the label : 10,65 cm x 8,20 cm > horizontal With different inlays like zeppelin, balloon, …
Should not have
• Funny decorations

```html
<!DOCTYPE html>
<html lang="en">
<head>
<meta charset="utf-8">
<title>Velmont Dry Gin – Label</title>
<link href="https://fonts.googleapis.com/css2?family=Cinzel:wght@400;600&family=Archivo+Narrow:wght@400&display=swap" rel="stylesheet">
<style>
  :root {
    --backdrop: #eceeef;
    --violet-deep: #2a2a6e;
    --violet-mid: #3b3590;
    --violet-light: #4a3f9c;
    --brass: #b77a2c;
    --brass-dark: #9a6526;
    --cream: #ece6f4;
    --leaf-green: #5fb04a;
    --wood-black: #1f140c;
    --wood-dark: #3a2414;
    --wood-mid: #6b4426;
    --wood-rust: #7a3f1e;
    --wood-light: #a07a52;
    --parchment: #b39270;
  }
  * { margin: 0; padding: 0; box-sizing: border-box; }
  html, body { width: 1200px; height: 1200px; overflow: hidden; }
  body {
    background: var(--backdrop);
    display: flex;
    align-items: center;
    justify-content: center;
  }
  .label {
    width: 1064px;
    height: 820px;
    display: grid;
    grid-template-columns: 245px 1fr 245px;
    box-shadow: 0 6px 24px rgba(0,0,0,.18);
  }
  .inlay { height: 100%; }
  .inlay--left {
    background:
      radial-gradient(ellipse 60% 30% at 35% 20%, rgba(122,63,30,.75) 0%, transparent 70%),
      radial-gradient(ellipse 70% 35% at 55% 70%, rgba(160,122,82,.55) 0%, transparent 75%),
      radial-gradient(ellipse 50% 25% at 30% 45%, rgba(31,20,12,.8) 0%, transparent 70%),
      linear-gradient(180deg, var(--wood-dark) 0%, var(--wood-mid) 55%, var(--wood-dark) 100%);
  }
  .inlay--right {
    background:
      radial-gradient(ellipse 60% 30% at 60% 25%, rgba(179,146,112,.8) 0%, transparent 70%),
      radial-gradient(ellipse 55% 30% at 40% 65%, rgba(58,36,20,.55) 0%, transparent 70%),
      radial-gradient(ellipse 60% 25% at 55% 88%, rgba(160,122,82,.7) 0%, transparent 75%),
      linear-gradient(180deg, var(--wood-light) 0%, var(--wood-mid) 60%, var(--wood-light) 100%);
  }
  .panel {
    position: relative;
    background: linear-gradient(160deg, var(--violet-light) 0%, var(--violet-mid) 45%, var(--violet-deep) 100%);
    display: flex;
    flex-direction: column;
    align-items: center;
    padding-top: 60px;
  }
  .brand {
    display: flex;
    flex-direction: column;
    align-items: center;
    gap: 16px;
  }
  .brand__dot {
    width: 90px;
    height: 90px;
    border-radius: 50%;
    background: var(--brass);
  }
  .brand__name {
    font-family: "Cinzel", serif;
    font-weight: 600;
    font-size: 30px;
    letter-spacing: 2px;
    color: var(--brass);
  }
  .brand__tagline {
    font-family: "Cinzel", serif;
    font-weight: 600;
    font-size: 12px;
    letter-spacing: 1.5px;
    color: var(--brass);
    margin-top: -6px;
    white-space: nowrap;
  }
  .divider {
    width: 240px;
    height: 2px;
    background: var(--brass-dark);
  }
  .divider--top { margin-top: 240px; }
  .divider--bottom { width: 110px; margin-top: 22px; }
  .product__name {
    font-family: "Cinzel", serif;
    font-weight: 600;
    font-size: 66px;
    letter-spacing: 3px;
    color: var(--brass);
    margin-top: 34px;
    line-height: 1;
  }
  .product__type {
    font-family: "Cinzel", serif;
    font-size: 44px;
    letter-spacing: 2px;
    color: var(--cream);
    margin-top: 10px;
    line-height: 1;
  }
  .spec {
    position: absolute;
    bottom: 44px;
    font-family: "Archivo Narrow", sans-serif;
    font-size: 24px;
    color: var(--leaf-green);
  }
  .spec--abv { left: 60px; }
  .spec--volume { right: 60px; }
</style>
</head>
<body>
  <main class="label">
    <div class="inlay inlay--left" role="img" aria-label="Weathered steampunk inlay with zeppelin and chemical bottles in dark brown and rust tones"></div>
    <section class="panel">
      <div class="brand">
        <span class="brand__dot"></span>
        <span class="brand__name">LE CABINET DORÉ</span>
        <span class="brand__tagline">AWAKEN YOUR SENSES - FOLLOW YOUR WONDER</span>
      </div>
      <span class="divider divider--top"></span>
      <h1 class="product__name">VELMONT</h1>
      <p class="product__type">DRY GIN</p>
      <span class="divider divider--bottom"></span>
      <span class="spec spec--abv">43% VOL</span>
      <span class="spec spec--volume">e50 CL</span>
    </section>
    <div class="inlay inlay--right" role="img" aria-label="Aged parchment steampunk inlay with hot-air balloon and botanical ingredients in sepia tones"></div>
  </main>
</body>
</html>
```